Business Card

Velmora Jewels Marisol Venkova Heritage Collection business card
Looking for a modern, classic and timeless business card for our jewelry company

Front of card should be a, all purple solid color for the background and white lettering like the attached document.

On the front of card:
Velmora Jewels
Marisol Venkova Heritage Collection
One of A Kind Designs for you!

Marisol Tervane
Owner

On the back on card
Email: studio.velmora@mailbrook.net
Facebook: https://www.friendspace.net/VelmoraJewelsStudio
Twitter:
https://chirpline.net/velmora_jw
Instagram: http://picturewall.net/velmorajewels

```html
<!DOCTYPE html>
<html lang="en">
<head>
<meta charset="utf-8">
<title>Velmora Jewels — Business Card</title>
<link href="https://fonts.googleapis.com/css2?family=Questrial&family=Montserrat:wght@700&display=swap" rel="stylesheet">
<style>
  :root {
    --stage: #2f3d46;
    --purple: #6a46a0;
    --purple-light: #9a82bf;
    --white: #ffffff;
    --silver-hi: #f2f2f4;
    --silver-mid: #dcdce0;
    --silver-lo: #b9b9c0;
    --tail: #a9a9b0;
    --tail-fold: #7d7d85;
    --ribbon-text: #6a46a0;
  }
  * { margin: 0; padding: 0; box-sizing: border-box; }
  html, body {
    width: 1200px; height: 1000px; overflow: hidden;
    background: var(--stage);
    font-family: "Questrial", "Century Gothic", sans-serif;
    color: var(--white);
  }
  .canvas { position: relative; width: 1200px; height: 1000px; }

  .card {
    position: absolute; left: 220px; width: 760px; height: 434px;
    background: var(--purple); overflow: hidden;
    box-shadow: 0 10px 30px rgba(0,0,0,0.35);
  }
  .card-back { top: 46px; }
  .card-front { top: 520px; }

  /* Back: contact bands */
  .contact-band {
    display: flex; align-items: center; height: 108.5px; padding-left: 40px;
    border-bottom: 1px solid rgba(255,255,255,0.25);
  }
  .contact-band:last-child { border-bottom: none; }
  .contact-band.is-dark { background: var(--purple); }
  .contact-band.is-light { background: var(--purple-light); }
  .contact-icon {
    width: 58px; height: 58px; border-radius: 10px; background: var(--white);
    flex: none; display: flex; align-items: center; justify-content: center;
  }
  .contact-text {
    margin-left: 60px; font-size: 23px; line-height: 1.2; letter-spacing: 0.3px;
  }

  /* Front */
  .brand-square {
    position: absolute; top: 30px; left: 338px; width: 84px; height: 84px;
    border: 2px solid var(--white);
  }
  .brand-name {
    position: absolute; top: 138px; left: 0; right: 0; text-align: center;
    font-weight: 400; font-size: 46px; letter-spacing: 2px; line-height: 1;
  }
  .collection-name {
    position: absolute; top: 190px; left: 0; right: 0; text-align: center;
    font-size: 24px; line-height: 1;
  }
  .established {
    position: absolute; top: 218px; left: 0; right: 0; text-align: center;
    font-size: 22px; letter-spacing: 3px; line-height: 1;
  }
  .ribbon { position: absolute; top: 250px; left: 110px; width: 540px; height: 72px; }
  .ribbon svg { position: absolute; inset: 0; }
  .ribbon-text {
    position: absolute; inset: 0 50px 10px; display: flex; align-items: center; justify-content: center;
    color: var(--ribbon-text); font-size: 27px;
  }
  .owner-line {
    position: absolute; top: 348px; left: 0; right: 0; text-align: center; line-height: 1;
  }
  .owner-name { font-family: "Montserrat", "Century Gothic", sans-serif; font-weight: 700; font-size: 31px; }
  .owner-role { font-size: 27px; margin-left: 8px; }
</style>
</head>
<body>
<main class="canvas">

  <section class="card card-back" aria-label="Business card back">
    <div class="contact-band is-dark">
      <span class="contact-icon">
        <svg width="38" height="28" viewBox="0 0 38 28" aria-label="Email">
          <rect x="2" y="2" width="34" height="24" fill="none" stroke="var(--purple)" stroke-width="3"/>
          <polyline points="2,2 19,16 36,2" fill="none" stroke="var(--purple)" stroke-width="3"/>
        </svg>
      </span>
      <p class="contact-text">studio.velmora@mailbrook.net</p>
    </div>
    <div class="contact-band is-light">
      <span class="contact-icon" aria-hidden="true"></span>
      <p class="contact-text">friendspace.net/<br>VelmoraJewelsStudio</p>
    </div>
    <div class="contact-band is-dark">
      <span class="contact-icon" aria-hidden="true"></span>
      <p class="contact-text">chirpline.net/<br>velmora_jw</p>
    </div>
    <div class="contact-band is-light">
      <span class="contact-icon" aria-hidden="true"></span>
      <p class="contact-text">picturewall.net/<br>velmorajewels</p>
    </div>
  </section>

  <section class="card card-front" aria-label="Business card front">
    <span class="brand-square" aria-hidden="true"></span>
    <h1 class="brand-name">Velmora Jewels</h1>
    <p class="collection-name">Marisol Venkova Heritage Collection</p>
    <p class="established">EST. 2014</p>
    <div class="ribbon">
      <svg viewBox="0 0 540 72" preserveAspectRatio="none" aria-hidden="true">
        <defs>
          <linearGradient id="silver" x1="0" y1="0" x2="1" y2="1">
            <stop offset="0" stop-color="var(--silver-hi)"/>
            <stop offset="0.5" stop-color="var(--silver-mid)"/>
            <stop offset="1" stop-color="var(--silver-lo)"/>
          </linearGradient>
        </defs>
        <polygon points="0,22 70,22 70,66 0,66 20,44" fill="var(--tail)"/>
        <polygon points="540,22 470,22 470,66 540,66 520,44" fill="var(--tail)"/>
        <polygon points="50,56 70,66 70,56" fill="var(--tail-fold)"/>
        <polygon points="490,56 470,66 470,56" fill="var(--tail-fold)"/>
        <rect x="50" y="6" width="440" height="50" fill="url(#silver)"/>
      </svg>
      <p class="ribbon-text">One of A Kind Designs for you!</p>
    </div>
    <p class="owner-line"><span class="owner-name">Marisol Tervane</span><span class="owner-role">Owner</span></p>
  </section>

</main>
</body>
</html>
```